New Word Template Design Project

I need this document for death certificate ordering to look like our branding. I will attach the pdf with the information and a sample pdf of our style. I also think that check boxes and x's would be better than yes and no.

2nd page in spanish.

Industry/Entity Type

Funeral

Requirements
Should not have
• Check boxes and red x's or yellow next to the yes, no , or sometimes

```html
<!DOCTYPE html>
<html lang="en">
<head>
<meta charset="utf-8">
<title>Death Certificate Ordering Guide – Harrow Lane</title>
<link href="https://fonts.googleapis.com/css2?family=Lobster&family=Roboto:ital,wght@0,400;0,500;0,700;1,400&display=swap" rel="stylesheet">
<style>
  :root{
    --brand:#4b6e88;
    --brand-dark:#47687f;
    --ink:#1f1f1f;
    --muted:#5b5b5b;
    --gold:#d6b25a;
    --rule:#c9c9c9;
    --ok:#2ea84a;
    --no:#e0262b;
    --paper:#ffffff;
  }
  *{box-sizing:border-box;margin:0;padding:0}
  html,body{width:927px;height:1200px;overflow:hidden}
  body{background:var(--brand);font-family:"Roboto",Arial,sans-serif;color:var(--ink);position:relative}
  .sheet{position:absolute;left:19px;top:19px;width:890px;height:1162px;background:var(--paper);overflow:hidden}
  .abs{position:absolute}

  .brand{left:36px;top:72px;width:250px;display:flex;align-items:center;gap:12px}
  .brand-mark{flex:none;width:14px;height:14px;border-radius:50%;background:var(--brand)}
  .brand-name{font-size:44px;font-weight:400;color:var(--brand);line-height:1;white-space:nowrap}

  .title-pill{left:345px;top:43px;width:560px;height:94px;background:var(--brand);border-radius:47px 0 0 47px;color:#fff;text-align:center;padding-top:6px}
  .title-pill h1{font-family:"Lobster",cursive;font-weight:400;font-size:37px;line-height:1.15}
  .title-pill p{font-size:26px;letter-spacing:.3px;margin-top:2px}

  .gold-rule{height:1.5px;background:linear-gradient(90deg,transparent,var(--gold) 15%,var(--gold) 85%,transparent)}
  .emblem{width:38px;height:34px;border-radius:50%;background:radial-gradient(circle,#c9b0d6,#8aa2c0 60%,transparent 72%)}

  .intro{left:20px;top:215px;width:850px;text-align:center;font-size:15px;line-height:27.6px;color:var(--muted)}

  .uses{left:33px;top:315px;width:822px;border-collapse:collapse;border:1px solid #9a9a9a;font-size:11.3px}
  .uses th{height:44px;font-weight:400;font-size:15.5px;border-left:1px solid #9a9a9a;border-bottom:1px solid var(--rule)}
  .uses th:first-child{text-align:left;padding-left:64px;border-left:none}
  .uses td{height:26.9px;border-bottom:1px solid var(--rule);border-left:1px solid #9a9a9a;padding:0}
  .uses td:first-child{padding-left:16px;border-left:none;width:249px}
  .uses td.ans{width:195px}
  .uses td.ans:nth-child(3){width:171px}
  .uses tr:last-child td{border-bottom:none;height:34px;vertical-align:top;padding-top:8px}
  .uses tr:first-child td{height:31px}
  .ans span{display:inline-flex;align-items:center;gap:7px;margin-left:56px}
  .uses td.ans:nth-child(3) span{margin-left:45px}
  .uses td.qty{padding-left:62px}
  .ico{width:12px;height:12px}

  .pricing{left:36px;top:808px;width:820px;font-size:13.6px;line-height:26px}
  .pricing h2{font-size:16px;font-weight:500;color:var(--brand);line-height:24px}
  .pricing p{text-align:justify}
  .order-q{font-size:16px;font-weight:500;color:var(--brand);line-height:24px}
  .blanks{left:36px;top:1072px;font-size:13.6px;line-height:26px}

  .footer{left:0;top:1072px;width:890px;height:90px}
  .footer-text{left:274px;top:1090px;color:#fff}
  .footer-text h3{font-size:16.5px;font-weight:700}
  .footer-text p{font-size:12.6px;line-height:20px;margin-top:12px}
  .contacts{left:550px;top:1082px;color:#fff;font-size:13px;line-height:19px;list-style:none}
  .contacts li{display:flex;align-items:center;gap:14px}
  .contacts svg{width:14px;height:14px;flex:none}
  .contacts li.plain{padding-left:28px}
  .page-no{right:6px;bottom:2px;color:#fff;font-size:10px}
</style>
</head>
<body>
<div class="sheet">
  <div class="abs brand">
    <span class="brand-mark"></span>
    <div class="brand-name">Harrow Lane</div>
  </div>

  <header class="abs title-pill">
    <h1>Death Certificate Ordering Guide</h1>
    <p>MIAMI-DADE COUNTY</p>
  </header>

  <div class="abs gold-rule" style="left:86px;top:184px;width:700px"></div>
  <div class="abs emblem" role="img" aria-label="Small decorative bird emblem" style="left:762px;top:167px"></div>

  <p class="abs intro">Certified death certificates are used to handle legal, financial, and personal matters after a loved one passes. While some institutions require an original, others may only need to view or copy it. In Florida, you can order death certificates with or without the cause of death. Cause of death is confidential and should only be included when necessary.</p>

  <svg width="0" height="0" style="position:absolute">
    <symbol id="tick" viewBox="0 0 12 12"><path d="M1.5 6.5l3 3 6-7" fill="none" stroke="#2ea84a" stroke-width="2.2" stroke-linecap="round" stroke-linejoin="round"/></symbol>
    <symbol id="cross" viewBox="0 0 12 12"><path d="M2.5 2.5l7 7M9.5 2.5l-7 7" stroke="#e0262b" stroke-width="2.2" stroke-linecap="round"/></symbol>
  </svg>

  <table class="abs uses">
    <thead><tr><th>Use</th><th>Original Needed?</th><th>With Cause?</th><th>Suggested Quantity</th></tr></thead>
    <tbody>
      <tr><td>Life Insurance Claims</td><td class="ans"><span><svg class="ico"><use href="#tick"/></svg>Yes</span></td><td class="ans"><span><svg class="ico"><use href="#tick"/></svg>Yes</span></td><td class="qty">1 per policy</td></tr>
      <tr><td>Pension or Retirement Benefits</td><td class="ans"><span><svg class="ico"><use href="#tick"/></svg>Yes</span></td><td class="ans"><span><svg class="ico"><use href="#tick"/></svg>Yes</span></td><td class="qty">1</td></tr>
      <tr><td>Bank Accounts</td><td class="ans"><span><svg class="ico"><use href="#cross"/></svg>Usually Not</span></td><td class="ans"><span><svg class="ico"><use href="#cross"/></svg>No</span></td><td class="qty">0–1</td></tr>
      <tr><td>Investment / Brokerage Accounts</td><td class="ans"><span><svg class="ico"><use href="#tick"/></svg>Sometimes</span></td><td class="ans"><span><svg class="ico"><use href="#tick"/></svg>Sometimes</span></td><td class="qty">1–2</td></tr>
      <tr><td>Vehicle Title Transfer (DMV)</td><td class="ans"><span><svg class="ico"><use href="#tick"/></svg>Yes</span></td><td class="ans"><span><svg class="ico"><use href="#cross"/></svg>No</span></td><td class="qty">1</td></tr>
      <tr><td>Property / Real Estate Transfers</td><td class="ans"><span><svg class="ico"><use href="#tick"/></svg>Yes</span></td><td class="ans"><span><svg class="ico"><use href="#cross"/></svg>No</span></td><td class="qty">1 per property</td></tr>
      <tr><td>Probate / Court Matters</td><td class="ans"><span><svg class="ico"><use href="#tick"/></svg>Yes</span></td><td class="ans"><span><svg class="ico"><use href="#tick"/></svg>Often</span></td><td class="qty">1–2</td></tr>
      <tr><td>Social Security / Government Benefits</td><td class="ans"><span><svg class="ico"><use href="#cross"/></svg>No</span></td><td class="ans"><span><svg class="ico"><use href="#tick"/></svg>Yes</span></td><td class="qty">1</td></tr>
      <tr><td>Passport Cancellation / Consulates</td><td class="ans"><span><svg class="ico"><use href="#tick"/></svg>Yes</span></td><td class="ans"><span><svg class="ico"><use href="#tick"/></svg>Yes</span></td><td class="qty">1</td></tr>
      <tr><td>Domestic Travel with Cremated Remains</td><td class="ans"><span><svg class="ico"><use href="#tick"/></svg>Yes</span></td><td class="ans"><span><svg class="ico"><use href="#cross"/></svg>No</span></td><td class="qty">1</td></tr>
      <tr><td>International Travel with Cremated Remains</td><td class="ans"><span><svg class="ico"><use href="#tick"/></svg>Yes</span></td><td class="ans"><span><svg class="ico"><use href="#tick"/></svg>Yes</span></td><td class="qty">1</td></tr>
      <tr><td>Domestic Forwarding of Remains</td><td class="ans"><span><svg class="ico"><use href="#tick"/></svg>Yes</span></td><td class="ans"><span><svg class="ico"><use href="#tick"/></svg>Sometimes</span></td><td class="qty">1</td></tr>
      <tr><td>International Forwarding of Remains</td><td class="ans"><span><svg class="ico"><use href="#tick"/></svg>Yes</span></td><td class="ans"><span><svg class="ico"><use href="#tick"/></svg>Yes</span></td><td class="qty">1</td></tr>
      <tr><td>Credit Cards / Utility Companies</td><td class="ans"><span><svg class="ico"><use href="#cross"/></svg>Usually Not</span></td><td class="ans"><span><svg class="ico"><use href="#cross"/></svg>No</span></td><td class="qty">0</td></tr>
      <tr><td>Personal Copy / Peace of Mind</td><td class="ans"><span><svg class="ico"><use href="#tick"/></svg>Optional</span></td><td class="ans"><span><svg class="ico"><use href="#tick"/></svg>Optional</span></td><td class="qty">1</td></tr>
    </tbody>
  </table>

  <section class="abs pricing">
    <h2>Pricing (Miami-Dade County):</h2>
    <p>The first certified death certificate is $20, and each additional copy is $16.</p>
    <p>If you are traveling domestically or internationally with cremated remains, at least one certified copy is typically required. Some countries may require the certificate with cause of death. We will reach out to the consulate of the destination country to confirm the specific requirements for transporting cremated remains.</p>
    <p>Please note: Other counties may have different pricing for death certificates. We will inform you of the exact cost based on the location of death.</p>
    <p>Most families order 4 to 8 certified copies. A mix is common — for example, 2 with cause and 4 without cause. It simpler and more cost-effective to order them at the time of need. If you're unsure, we are here to guide you through the process.</p>
    <div class="order-q">How many certified copies would you like to order?</div>
  </section>

  <div class="abs gold-rule" style="left:424px;top:1063px;width:430px"></div>
  <div class="abs emblem" role="img" aria-label="Small decorative bird emblem" style="left:834px;top:1027px"></div>

  <svg class="abs footer" viewBox="0 0 890 90" preserveAspectRatio="none" aria-hidden="true">
    <polygon points="265,0 890,0 890,90 207,90" fill="var(--brand-dark)"/>
  </svg>

  <div class="abs blanks">
    <div>____ With Cause of Death</div>
    <div>____ Without Cause of Death</div>
  </div>

  <div class="abs footer-text">
    <h3>Questions? We’re Here for You</h3>
    <p>Serving Miami-Dade County with care,<br>dignity, and support for over 100 years.</p>
  </div>

  <ul class="abs contacts">
    <li><svg viewBox="0 0 24 24"><path fill="#fff" d="M6.6 10.8a15.5 15.5 0 0 0 6.6 6.6l2.2-2.2c.3-.3.7-.4 1-.2 1.1.4 2.3.6 3.6.6.6 0 1 .4 1 1V20c0 .6-.4 1-1 1C10.6 21 3 13.4 3 4c0-.6.4-1 1-1h3.5c.6 0 1 .4 1 1 0 1.3.2 2.5.6 3.6.1.3 0 .7-.2 1z"/></svg>(305) 555-0142</li>
    <li><svg viewBox="0 0 24 24"><path fill="#fff" d="M3 5h18v14H3z"/><path d="M3 6l9 7 9-7" fill="none" stroke="#47687f" stroke-width="2"/></svg>kendall@harrowlane.com | midtown@harrowlane.com</li>
    <li><svg viewBox="0 0 24 24"><circle cx="12" cy="12" r="9" fill="#fff"/><path d="M3 12h18M12 3c3 3 3 15 0 18M12 3c-3 3-3 15 0 18" fill="none" stroke="#47687f" stroke-width="1.5"/></svg>coralgables@harrowlane.com</li>
    <li class="plain">preplanning@harrowlane.com</li>
  </ul>
</div>
<div class="abs page-no">C9</div>
</body>
</html>
```